Création de la plaquette commerciale de la VTR
Besoins
Nous avons besoin d'une plaquette commerciale décrivant l'ensemble des activités de notre entreprise tout en montrant notre dynamisme, notre professionnalisme et disponibilité.
Description de l'entreprise
La V.T.R. est une société de services en ingénierie informatique dont les activités sont :
. INGÉNIERIE : Audit des systèmes d'information, Conseil en informatique et système d'information, Ingénierie informatique (conception, développement, fabrication de système d'information
. INTERNET : Conception et design de site web, hébergement internet
. VAR : Revendeur à valeur ajoutée (matériels, logiciels, périphériques, consommables, ...)
. MAINTENANCE : Maintenance sur site avec contrat
Notre site internet :
www.vtr-lomapo.net
La cible
Notre cible est l'ensemble des professionnels et plus particulièrement les TPE, PME & PMI
Couleurs, favoris et autres exigences:
Notre besoin est :
. une plaquette commerciale au format A3 plié en 2 pour les 4 activités
. des feuillets pour les références ingénierie, web, sociétés

```html
<!DOCTYPE html>
<html lang="fr">
<head>
<meta charset="utf-8">
<title>VTR – plaquette commerciale</title>
<link href="https://fonts.googleapis.com/css2?family=Arimo:ital,wght@0,400;0,700;1,400;1,700&display=swap" rel="stylesheet">
<style>
:root{
  --teal:#1f9aa3;
  --teal-dark:#0f7480;
  --teal-light:#8fd0d4;
  --teal-pale:#dff1f2;
  --ink:#3b3b3b;
  --grey:#8a8a8a;
  --white:#ffffff;
}
*{box-sizing:border-box;margin:0;padding:0}
html,body{width:1200px;height:860px;overflow:hidden;background:var(--white)}
body{font-family:"Arimo",Arial,sans-serif;color:var(--ink);position:relative}
.abs{position:absolute}
p{line-height:1.35}

/* ---- outside cover ---- */
.trust{left:20px;top:12px;font-size:11px;font-style:italic;font-weight:700;color:var(--teal)}
.client{top:136px;height:46px;display:flex;align-items:center;justify-content:center;font-size:11px;font-weight:700;color:var(--teal-dark)}
.client-box{border:1px solid var(--teal-light)}
.badge{width:44px;height:44px;border-radius:50%;background:var(--teal-light)}
.seal{left:250px;top:192px;width:128px;height:128px;border-radius:50%;border:3px solid var(--teal);display:flex;align-items:center;justify-content:center;font-size:30px;font-weight:700;color:var(--teal-dark)}
.identity{left:150px;top:332px;width:300px;text-align:center;font-size:11px;font-weight:700;color:var(--teal-dark);line-height:1.45}
.identity .name{font-size:14px;font-style:italic}

.mosaic{left:600px;top:130px;width:600px;height:265px;background:linear-gradient(100deg,var(--teal-pale) 0%,var(--teal-light) 35%,var(--teal) 70%,var(--teal-dark) 100%)}
.cover-seal{left:790px;top:40px;width:160px;height:160px;border-radius:50%;border:4px solid var(--teal);background:var(--white);display:flex;align-items:center;justify-content:center;font-size:40px;font-weight:700;color:var(--teal-dark)}
.tagline{left:780px;top:404px;font-size:13px;color:var(--teal)}

/* ---- inside spread ---- */
.fold{left:0;top:436px;width:1200px;height:1px;background:var(--teal-pale)}
.president{left:0;top:440px;width:140px;height:420px;background:linear-gradient(180deg,var(--teal-light),var(--teal))}
.president .frame{position:absolute;left:50px;top:112px;width:32px;height:32px;background:var(--white)}
.president h3{position:absolute;left:12px;top:170px;font-family:Georgia,serif;font-style:italic;font-weight:400;font-size:13px;color:var(--white)}
.president p{position:absolute;left:10px;top:190px;width:120px;font-size:7.5px;color:var(--white)}

.band{left:140px;top:440px;width:890px;height:26px;background:linear-gradient(90deg,var(--teal),var(--teal-light))}
.tab{top:448px;height:22px;padding:0 18px;background:var(--teal-dark);color:var(--white);font-weight:700;font-size:13px;line-height:22px;border-radius:3px}
.intro{top:480px;width:410px;font-size:7.5px;color:var(--grey)}
.tile{top:518px;width:110px;height:72px}
.svc{top:596px;width:120px;font-size:7px;color:var(--grey)}
.svc b{display:block;color:var(--teal-dark);font-size:8.5px;margin-bottom:2px}

.sec-head{top:736px;font-size:14px;font-weight:700;color:var(--teal-dark);padding:3px 24px;background:var(--teal-pale);border-radius:3px}
.var{left:140px;top:758px;width:540px;height:84px;background:var(--teal)}
.var p{position:absolute;left:14px;top:6px;width:510px;font-size:7.5px;color:var(--white)}
.var .cat{position:absolute;top:30px;font-size:8px;font-weight:700;color:var(--white)}
.partners{position:absolute;left:14px;top:48px;display:flex;gap:10px}
.partners span{width:46px;height:22px;background:var(--white);border-radius:2px}
.maint{left:690px;top:758px;width:340px;height:84px;background:var(--teal-pale)}
.maint p{position:absolute;top:6px;width:155px;font-size:7px;color:var(--ink)}
.footer{left:140px;top:842px;width:890px;height:18px;background:var(--teal-dark);color:var(--white);font-size:10px;font-weight:700;font-style:italic;padding:3px 14px}

.side{left:1030px;top:440px;width:170px;height:420px;background:linear-gradient(180deg,var(--teal-pale),var(--white))}
.plus{left:1040px;top:462px;width:30px;height:30px;border:2px solid var(--teal);background:var(--white)}
.side h4{position:absolute;left:12px;font-size:8px;font-weight:700;color:var(--teal-dark)}
.side p{position:absolute;left:12px;width:148px;font-size:7px;color:var(--grey)}
.side .row{position:absolute;left:12px;width:148px;height:16px;background:var(--teal);color:var(--white);font-size:6.5px;padding:4px 6px}
</style>
</head>
<body>

<!-- Outside: back panel -->
<p class="abs trust">Ils nous ont fait confiance alors pourquoi pas vous ...</p>
<div class="abs client client-box" style="left:40px;width:90px">CGN Lomapo</div>
<div class="abs client" style="left:190px;width:50px"><span class="badge"></span></div>
<div class="abs client" style="left:285px;width:70px">Régie Eau</div>
<div class="abs client" style="left:435px;width:50px"><span class="badge"></span></div>
<div class="abs client client-box" style="left:530px;width:64px">Lomavie</div>
<div class="abs seal">VTR</div>
<div class="abs identity">
  <div class="name">Société Vectorielle de Réseaux</div>
  <div>V.T.R.</div>
  <div>Adresse : B.P. 1204</div>
  <div>Lomapo - Centre</div>
  <div>tel : +241 00 12 34 56 - Gsm : +241 00 65 43 21</div>
  <div>contact@vtr-lomapo.net</div>
</div>

<!-- Outside: front cover -->
<div class="abs mosaic" role="img" aria-label="Mosaïque de carrés turquoise en dégradé"></div>
<div class="abs cover-seal">VTR</div>
<p class="abs tagline">Ingénierie - Internet - VAR - Maintenance</p>

<div class="abs fold"></div>

<!-- Inside: president -->
<aside class="abs president">
  <span class="frame"></span>
  <h3>Le Mot du Président</h3>
  <p>Notre équipe accompagne chaque jour les entreprises de la région dans leurs projets informatiques. Nous mettons notre savoir-faire au service des TPE, PME et PMI avec la même exigence de qualité. Disponibles et réactifs, nos ingénieurs vous conseillent, installent et maintiennent vos équipements. Nous croyons à une relation durable fondée sur la confiance et la proximité. Notre ambition est de faire de votre système d'information un véritable atout pour votre croissance. Nous vous remercions de votre confiance et restons à votre écoute pour tout nouveau projet.</p>
</aside>

<!-- Inside: services -->
<div class="abs band"></div>
<div class="abs tab" style="left:318px">Ingénierie</div>
<div class="abs tab" style="left:738px">Internet</div>
<p class="abs intro" style="left:170px">Le pôle ingénierie de V.T.R. accompagne votre entreprise de l'audit à la conception de votre système d'information, avec des méthodes éprouvées et une équipe qualifiée.</p>
<p class="abs intro" style="left:592px">V.T.R. conçoit et héberge vos sites web, du site vitrine à la boutique en ligne, avec un design soigné et une sécurité adaptée à votre activité.</p>

<div class="abs tile" role="img" aria-label="Photo audit informatique" style="left:172px;background:linear-gradient(135deg,#cfd8dc,#7fa4ad)"></div>
<div class="abs tile" role="img" aria-label="Photo conseil en entreprise" style="left:312px;background:linear-gradient(135deg,#e0e0e0,#8e9ea3)"></div>
<div class="abs tile" role="img" aria-label="Photo conception de système" style="left:452px;background:linear-gradient(135deg,#d6e4e8,#5e8c97)"></div>
<div class="abs tile" role="img" aria-label="Photo chantier de site web" style="left:592px;background:linear-gradient(135deg,#f0ead8,#b9a878)"></div>
<div class="abs tile" role="img" aria-label="Photo commerce en ligne" style="left:732px;background:linear-gradient(135deg,#eef5d6,#9cc24c)"></div>
<div class="abs tile" role="img" aria-label="Photo sécurité informatique" style="left:872px;background:linear-gradient(135deg,#dfe8ee,#6b8aa3)"></div>

<p class="abs svc" style="left:172px"><b>AUDIT</b>Analyse de votre parc et de vos processus pour identifier les points à améliorer et les risques.</p>
<p class="abs svc" style="left:312px"><b>CONSEIL</b>Des recommandations claires pour choisir les bonnes solutions et maîtriser vos budgets.</p>
<p class="abs svc" style="left:452px"><b>CONCEPTION</b>Conception, développement et mise en place de systèmes d'information sur mesure.</p>
<p class="abs svc" style="left:592px"><b>WEBSITE</b>Création de sites modernes, simples à mettre à jour et visibles sur tous les écrans.</p>
<p class="abs svc" style="left:732px"><b>e-COMMERCE</b>Boutiques en ligne complètes avec catalogue, panier et paiement sécurisé intégré.</p>
<p class="abs svc" style="left:872px"><b>SECURITE</b>Protection de vos données et de vos sites contre les intrusions et les pannes.</p>

<div class="abs sec-head" style="left:360px">V.A.R.</div>
<div class="abs sec-head" style="left:750px">Maintenance</div>

<section class="abs var">
  <p>V.A.R. est revendeur à valeur ajoutée : nous fournissons matériels, logiciels, périphériques et consommables, et nous en assurons l'installation et la configuration sur votre site.</p>
  <span class="cat" style="left:14px">ORDINATEURS</span>
  <span class="cat" style="left:170px">LOGICIELS</span>
  <span class="cat" style="left:282px">SECURITE</span>
  <div class="partners"><span></span><span></span><span></span><span></span><span></span><span></span><span></span></div>
</section>

<section class="abs maint">
  <p style="left:12px">• Curative<br>Intervention rapide sur site dès le signalement d'une panne et remise en service.<br>• Préventive<br>Visites planifiées pour contrôler vos postes et réseaux.</p>
  <p style="left:176px">Un contrat adapté à votre parc garantit des délais fixes.<br>• Evolutive<br>Mises à jour régulières de vos logiciels et de vos matériels.</p>
</section>

<p class="abs footer">et bien d'autres ! Alors n'hésitez plus et contactez-nous au +241 00 12 34 56 - www.vtr-lomapo.net</p>

<!-- Inside: sidebar -->
<aside class="abs side">
  <h4 style="top:60px">HEBERGEMENT</h4>
  <p style="top:72px">Hébergement sécurisé de vos sites et messageries sur des serveurs performants, avec sauvegarde quotidienne et assistance.</p>
  <div role="img" aria-label="Illustration moteurs de recherche" style="position:absolute;left:12px;top:190px;width:148px;height:70px;background:linear-gradient(135deg,#ffffff,var(--teal-light))"></div>
  <h4 style="top:282px">REFERENCEMENT</h4>
  <p style="top:294px">Nous améliorons la visibilité de votre site.</p>
  <div class="row" style="top:314px">Référencement naturel</div>
  <div class="row" style="top:336px">Référencement payant</div>
  <div class="row" style="top:358px">Suivi des positions</div>
  <div class="row" style="top:380px">Rapports mensuels</div>
</aside>
<div class="abs plus"></div>

</body>
</html>
```